Redesign a programmers open source website

This is a fairly old website (started 1999) that hosts lots of programming-related stuff, from the useful (freeware tools, articles on programming topics) to the obscure (esoteric programming languages, tips on code obfuscation and bad examples), plus a couple of other bits thrown in. It is 100% open source and free. However, it looks a bit boring, so I want to liven up the design, and make it the basis for a future portfolio showcase. The design should be compatible with bootstrap (i.e. work on mobile devices).

Take a look at the existing one over at
http://q-vorl-z.net

Target Market(s)

Software Companies

Coding

Coded - Design and coding required

Number of Pages Required

2 page

Font styles to use
Sans Serif

Requirements
Must have
• After reviewing the designs submitted so far:
• - something reduced and elegant
• - something that is not too noisy, but instead reflects quality.
• - I would like to see two pages: the frontpage, and one text-heavy (for example, an article on one of my programming languages).

```html
<!DOCTYPE html>
<html lang="en">
<head>
<meta charset="utf-8">
<title>q-vorl-z.net – Languages</title>
<link rel="stylesheet" href="https://fonts.googleapis.com/css2?family=PT+Sans:ital,wght@0,400;0,700;1,400&display=swap">
<style>
  :root{
    --page-bg:#e5e5e5;
    --white:#ffffff;
    --nav-link:#3a8fd0;
    --link:#2f7fc6;
    --title-green:#3f7f3a;
    --teal:#3dbf8a;
    --red-rule:#e0645a;
    --text:#2b2b2b;
    --muted:#6a6a6a;
    --button:#4caf50;
    --border:#d6d6d6;
    --footer:#4a4a4a;
    --footer-top:#3f3f3f;
    --hero-dark:#12380f;
    --hero-mid:#2f7a22;
    --hero-light:#58c247;
    --brand:#b04a9c;
    --tile-blue:#1565c0;
    --circuit-blue:#1a3d8f;
  }
  *{box-sizing:border-box;margin:0;padding:0}
  html,body{width:1200px;height:2687px;overflow:hidden}
  body{position:relative;background:var(--page-bg);font-family:"PT Sans",sans-serif;color:var(--text)}
  a{color:var(--link);text-decoration:none}

  /* navigation */
  .site-nav{position:absolute;left:0;top:0;width:1200px;height:63px;background:var(--white);border-bottom:1px solid var(--border)}
  .brand{position:absolute;left:14px;top:17px;display:flex;align-items:center;gap:8px;font-size:20px;font-weight:700;color:var(--brand)}
  .brand-mark{width:18px;height:18px;background:var(--brand);border-radius:3px}
  .nav-item{position:absolute;top:19px;font-size:16px;color:var(--nav-link)}
  .nav-item::after{content:" ▾";font-size:11px}
  .search{position:absolute;left:967px;top:13px;width:154px;height:29px;border:1px solid var(--border);border-radius:3px;font-size:12px;color:#888;padding:6px 10px}
  .login{position:absolute;left:1148px;top:19px;font-size:16px;color:var(--nav-link)}

  /* hero */
  .hero{position:absolute;left:0;top:63px;width:1200px;height:376px;background:linear-gradient(100deg,var(--hero-dark) 0%,var(--hero-mid) 55%,var(--hero-light) 100%);overflow:hidden}
  .hero-title{position:absolute;left:99px;top:60px;font-size:43px;font-weight:400;color:var(--white);letter-spacing:1px}
  .hero-line{position:absolute;left:99px;font-size:28px;color:var(--white)}
  .device{position:absolute;left:663px;top:111px;width:426px;height:202px;background:#111;border-radius:28px;box-shadow:0 4px 14px rgba(0,0,0,.45)}
  .device-screen{position:absolute;left:48px;top:14px;width:334px;height:174px;background:var(--white);display:flex;align-items:center;justify-content:center;font-size:40px;color:var(--brand)}
  .device-dots{position:absolute;left:0;right:0;bottom:22px;display:flex;justify-content:center;gap:12px}
  .device-dots span,.hero-dots span{width:7px;height:7px;border-radius:50%;background:#222}
  .device-dots span.off{background:none;border:1px solid #888}
  .hero-dots{position:absolute;left:560px;top:337px;display:flex;gap:17px}

  /* intro */
  .intro{position:absolute;left:192px;top:466px;width:906px}
  .intro h1{font-size:27px;font-weight:400;color:var(--teal);margin-bottom:4px}
  .intro p{font-size:18.5px;line-height:28.5px;text-align:justify}
  .intro ul{list-style:none;font-size:18.5px;line-height:28.5px;margin-top:14px}
  .intro-rule{position:absolute;left:93px;top:743px;width:1014px;border-top:1px solid var(--teal)}

  /* articles */
  .article{position:absolute;left:93px;width:663px;height:290px;background:var(--white);padding:12px 14px}
  .article h2{font-size:28px;font-weight:400;color:var(--title-green);line-height:34px}
  .meta{font-size:10px;color:var(--link);margin-top:4px}
  .meta span{color:var(--muted)}
  .excerpt{position:absolute;top:86px;width:370px;font-size:13.5px;line-height:21.5px}
  .excerpt .more{display:inline-block;margin-top:4px;background:var(--button);color:var(--white);font-size:13px;padding:2px 6px}
  .img-right .excerpt{left:14px}
  .img-right .excerpt .wrap{text-align:right}
  .img-left .excerpt{left:278px;width:368px}
  .thumb{position:absolute;top:78px;width:251px;height:192px}
  .img-right .thumb{left:398px;background:var(--tile-blue)}
  .img-left .thumb{left:14px;background:linear-gradient(135deg,#0b1f5c,var(--circuit-blue) 50%,#3a70d0)}
  .stub{position:absolute;left:93px;width:663px;height:18px;background:var(--white)}
  .stub::after{content:"";position:absolute;left:14px;top:8px;width:467px;border-top:1px solid #555}

  /* sidebar */
  .side-title{position:absolute;left:797px;width:310px;font-size:25px;font-weight:400;padding-bottom:3px;border-bottom:1px solid var(--red-rule)}
  .social{position:absolute;left:800px;top:815px;display:flex;gap:3px}
  .social span{width:40px;height:40px;border-radius:50%;border:2px solid #ddd}
  .social .s1{background:#3b5a9a}.social .s2{background:#2aa3e0}.social .s3{background:#d44a38}.social .s4{background:#1e78b3}.social .s5{background:#c8232c}
  .panel{position:absolute;left:797px;width:310px;background:var(--white);border:1px solid var(--border)}
  .recent li{list-style:none;height:59px;border-bottom:1px solid var(--border);padding:10px 12px 0 12px;font-size:13.5px;line-height:20px;color:var(--link)}
  .recent li:last-child{border-bottom:none}
  .recent b{font-weight:700}
  .recent svg{vertical-align:-2px;margin-right:6px}
  .cat-head{position:absolute;left:12px;font-size:13px;font-weight:400}
  .cat-head svg,.archive svg{vertical-align:-2px;margin-right:8px}
  .cat-list{position:absolute;left:30px;width:266px;border:1px solid var(--border);list-style:none}
  .cat-list li{height:39px;border-bottom:1px solid var(--border);padding:10px 0 0 32px;font-size:13px;color:var(--link)}
  .cat-list li:last-child{border-bottom:none}
  .cat-sep{position:absolute;left:0;width:308px;border-top:1px solid var(--border)}
  .archive li{list-style:none;height:39px;border-bottom:1px solid var(--border);padding:10px 0 0 12px;font-size:13px;color:var(--link)}
  .archive li:last-child{border-bottom:none}
  .archive-more{position:absolute;left:1039px;top:2357px;width:68px;height:34px;background:var(--white);font-size:13px;font-weight:700;color:var(--link);text-align:center;line-height:34px}

  /* footer */
  .site-footer{position:absolute;left:0;top:2421px;width:1200px;height:266px;background:var(--footer);border-top:3px solid var(--footer-top);font-size:11.5px;color:#e0e0e0}
  .site-footer .copy{position:absolute;left:59px;top:13px}
  .site-footer .copy a,.site-footer .links a{color:#4aa3e6}
  .site-footer .links{position:absolute;left:1063px;top:13px}
</style>
</head>
<body>

<header class="site-nav">
  <div class="brand"><span class="brand-mark"></span>q-vorl-z.net</div>
  <span class="nav-item" style="left:174px">Programming</span>
  <span class="nav-item" style="left:306px">Languages</span>
  <span class="nav-item" style="left:417px">Obfuscation</span>
  <span class="nav-item" style="left:541px">Downloads</span>
  <span class="nav-item" style="left:654px">Interests</span>
  <div class="search">Search</div>
  <span class="login">Login</span>
</header>

<section class="hero" role="img" aria-label="Green abstract swirl background behind the languages slide">
  <h2 class="hero-title">LANGUAGES</h2>
  <p class="hero-line" style="top:120px">Lorem ipsum dolor sit amet, consectetur</p>
  <p class="hero-line" style="top:166px">Lorem ipsum dolor sit amet, consectetur</p>
  <p class="hero-line" style="top:213px">Lorem ipsum dolor sit amet, consectetur</p>
  <p class="hero-line" style="top:259px">Lorem ipsum dolor sit amet, consectetur</p>
  <div class="device">
    <div class="device-screen">q-vorl-z.net</div>
    <div class="device-dots"><span></span><span></span><span class="off"></span><span></span></div>
  </div>
  <div class="hero-dots"><span></span><span></span><span></span><span></span></div>
</section>

<section class="intro">
  <h1>A bewildering assortment of <em>False</em></h1>
  <p>Welcome to my website, freshly redesigned for reading on mobile devices. I am still working on refreshing many of the old pages - for example, porting Viper 2.3 code from way pack to more current revisions; updating page styles and so on. Bear with me, this is work in progress...</p>
  <ul>
    <li>Well, on these pages you'll find</li>
    <li>- <a href="#">Programming Languages</a> that feature the logical operation NAND and other <a href="#">serious inventions</a>.</li>
    <li>- Loads of neat <a href="#">Fenestra</a>, <a href="#">Tuxix</a> and <a href="#">Pomme</a> utilities free for downloading.</li>
    <li>- The <a href="#">Viper Ministry of silly scripting</a></li>
  </ul>
</section>
<div class="intro-rule"></div>

<main>
  <article class="article img-right" style="top:774px">
    <h2>Using C++ Member Functions for C Function Pointers</h2>
    <p class="meta"><span>May 20, 2015 | </span>Programming » C/C++</p>
    <div class="excerpt">The consensus on the internet is that you cannot pass C++ member function pointers to functions expecting C function pointers.<br>For example, a typical question is <a href="#">How to pass a method to qsort?</a>, and the answer marked as "correct" says you should provide the address of a <em>static</em> function. Clearly that is too easy: static class member functions are mostly the same as plain old C functions, so in a way that answer is simply...<div class="wrap"><a class="more" href="#">Continue Reading</a></div></div>
    <div class="thumb" role="img" aria-label="Blue poster tile reading Learn programing and show who you are"></div>
  </article>

  <article class="article img-left" style="top:1109px">
    <h2>Using C++ Member Functions for C Function Pointers</h2>
    <p class="meta"><span>May 20, 2015 | </span>Programming » C/C++</p>
    <div class="excerpt">The consensus on the internet is that you cannot pass C++ member function pointers to functions expecting C function pointers.<br>For example, a typical question is <a href="#">How to pass a method to qsort?</a>, and the answer marked as "correct" says you should provide the address of a <em>static</em> function. Clearly that is too easy: static class member functions are mostly the same as plain old C functions, so in a way that answer is simply...<div><a class="more" href="#">Continue Reading</a></div></div>
    <div class="thumb" role="img" aria-label="Blue glowing code and circuit illustration"></div>
  </article>

  <article class="article img-right" style="top:1445px">
    <h2>Using C++ Member Functions for C Function Pointers</h2>
    <p class="meta"><span>May 20, 2015 | </span>Programming » C/C++</p>
    <div class="excerpt">The consensus on the internet is that you cannot pass C++ member function pointers to functions expecting C function pointers.<br>For example, a typical question is <a href="#">How to pass a method to qsort?</a>, and the answer marked as "correct" says you should provide the address of a <em>static</em> function. Clearly that is too easy: static class member functions are mostly the same as plain old C functions, so in a way that answer is simply...<div class="wrap"><a class="more" href="#">Continue Reading</a></div></div>
    <div class="thumb" role="img" aria-label="Blue poster tile reading Learn programing and show who you are"></div>
  </article>

  <article class="article img-left" style="top:1780px">
    <h2>Using C++ Member Functions for C Function Pointers</h2>
    <p class="meta"><span>May 20, 2015 | </span>Programming » C/C++</p>
    <div class="excerpt">The consensus on the internet is that you cannot pass C++ member function pointers to functions expecting C function pointers.<br>For example, a typical question is <a href="#">How to pass a method to qsort?</a>, and the answer marked as "correct" says you should provide the address of a <em>static</em> function. Clearly that is too easy: static class member functions are mostly the same as plain old C functions, so in a way that answer is simply...<div><a class="more" href="#">Continue Reading</a></div></div>
    <div class="thumb" role="img" aria-label="Blue glowing code and circuit illustration"></div>
  </article>

  <div class="stub" style="top:2099px"></div>
  <div class="stub" style="top:2137px"></div>
  <div class="stub" style="top:2175px"></div>
  <div class="stub" style="top:2214px"></div>
</main>

<aside>
  <h3 class="side-title" style="top:766px">Follow me on</h3>
  <div class="social"><span class="s1"></span><span class="s2"></span><span class="s3"></span><span class="s4"></span><span class="s5"></span></div>

  <h3 class="side-title" style="top:888px">Recent Articles</h3>
  <ul class="panel recent" style="top:944px">
    <li><svg width="13" height="13" viewBox="0 0 14 14"><circle cx="7" cy="7" r="7" fill="#222"/><path d="M4 7h6M7.5 4.5L10 7l-2.5 2.5" stroke="#fff" stroke-width="1.6" fill="none"/></svg><b>JUSTIF &amp; RECURSION</b> is an experiment in language minimalism</li>
    <li><svg width="13" height="13" viewBox="0 0 14 14"><circle cx="7" cy="7" r="7" fill="#222"/><path d="M4 7h6M7.5 4.5L10 7l-2.5 2.5" stroke="#fff" stroke-width="1.6" fill="none"/></svg><b>JUSTIF &amp; RECURSION</b> is an experiment in language minimalism</li>
    <li><svg width="13" height="13" viewBox="0 0 14 14"><circle cx="7" cy="7" r="7" fill="#222"/><path d="M4 7h6M7.5 4.5L10 7l-2.5 2.5" stroke="#fff" stroke-width="1.6" fill="none"/></svg><b>JUSTIF &amp; RECURSION</b> is an experiment in language minimalism</li>
    <li><svg width="13" height="13" viewBox="0 0 14 14"><circle cx="7" cy="7" r="7" fill="#222"/><path d="M4 7h6M7.5 4.5L10 7l-2.5 2.5" stroke="#fff" stroke-width="1.6" fill="none"/></svg><b>JUSTIF &amp; RECURSION</b> is an experiment in language minimalism</li>
    <li><svg width="13" height="13" viewBox="0 0 14 14"><circle cx="7" cy="7" r="7" fill="#222"/><path d="M4 7h6M7.5 4.5L10 7l-2.5 2.5" stroke="#fff" stroke-width="1.6" fill="none"/></svg><b>JUSTIF &amp; RECURSION</b> is an experiment in language minimalism</li>
  </ul>

  <h3 class="side-title" style="top:1297px">Categories</h3>
  <div class="panel categories" style="top:1349px;height:698px">
    <div class="cat-head" style="top:12px"><svg width="12" height="11" viewBox="0 0 12 11"><path d="M0 0h3v3H0zM4 0h8v3H4zM0 4h3v3H0zM4 4h8v3H4zM0 8h3v3H0zM4 8h8v3H4z" fill="#222"/></svg>Programming</div>
    <ul class="cat-list" style="top:49px"><li>C/C++</li><li>Viper</li><li>Fenestra</li><li>More...</li></ul>
    <div class="cat-sep" style="top:233px"></div>
    <div class="cat-head" style="top:244px"><svg width="12" height="11" viewBox="0 0 12 11"><path d="M0 0h3v3H0zM4 0h8v3H4zM0 4h3v3H0zM4 4h8v3H4zM0 8h3v3H0zM4 8h8v3H4z" fill="#222"/></svg>Languages</div>
    <ul class="cat-list" style="top:282px"><li>C/C++</li><li>Viper</li><li>Fenestra</li><li>More...</li></ul>
    <div class="cat-sep" style="top:466px"></div>
    <div class="cat-head" style="top:476px"><svg width="12" height="11" viewBox="0 0 12 11"><path d="M0 0h3v3H0zM4 0h8v3H4zM0 4h3v3H0zM4 4h8v3H4zM0 8h3v3H0zM4 8h8v3H4z" fill="#222"/></svg>Obfuscation</div>
    <ul class="cat-list" style="top:513px"><li>C/C++</li><li>Viper</li><li>Fenestra</li><li>More...</li></ul>
  </div>

  <h3 class="side-title" style="top:2103px">Archive</h3>
  <ul class="panel archive" style="top:2158px">
    <li><svg width="12" height="12" viewBox="0 0 12 12"><path d="M0 2h12v10H0z" fill="#222"/><path d="M1 5h10v6H1z" fill="#fff"/><path d="M2 0h2v3H2zM8 0h2v3H8z" fill="#222"/></svg>May 2015</li>
    <li><svg width="12" height="12" viewBox="0 0 12 12"><path d="M0 2h12v10H0z" fill="#222"/><path d="M1 5h10v6H1z" fill="#fff"/><path d="M2 0h2v3H2zM8 0h2v3H8z" fill="#222"/></svg>April 2015</li>
    <li><svg width="12" height="12" viewBox="0 0 12 12"><path d="M0 2h12v10H0z" fill="#222"/><path d="M1 5h10v6H1z" fill="#fff"/><path d="M2 0h2v3H2zM8 0h2v3H8z" fill="#222"/></svg>January 2015</li>
    <li><svg width="12" height="12" viewBox="0 0 12 12"><path d="M0 2h12v10H0z" fill="#222"/><path d="M1 5h10v6H1z" fill="#fff"/><path d="M2 0h2v3H2zM8 0h2v3H8z" fill="#222"/></svg>September 2014</li>
    <li><svg width="12" height="12" viewBox="0 0 12 12"><path d="M0 2h12v10H0z" fill="#222"/><path d="M1 5h10v6H1z" fill="#fff"/><path d="M2 0h2v3H2zM8 0h2v3H8z" fill="#222"/></svg>June 2014</li>
  </ul>
  <a class="archive-more" href="#">More...</a>
</aside>

<footer class="site-footer">
  <p class="copy">© 2000 to 2015 - All rights reserved. <a href="#">Terms and Conditions</a></p>
  <p class="links"><a href="#">Home</a> | <a href="#">About</a></p>
</footer>

</body>
</html>
```